Viral Marketing Software - Web Application Design

*****UPDATE******
Thank you all for your submissions but we would like to see more of a variety in these designs. It seems as though every design we have received has been almost identical to the mock up we provided. We would like to see more creativity. The mock up provided was meant to be used as an example not a format. We would appreciate if you could show us
1. Logo for Ripple Kindler
2. Home page design
3. Coupon Manager design

* Please refer to this link to see what our coupon manager page looks like.
http://qtrplaza.net/briefhub.html (use only as example please do not copy)
*******************************************************

We need a web design for a company based just outside of Austin, Texas called 'Ripple Kindler'. We have designed a viral marketing platform that harnesses the power of social media to spread promotions through people's social networks.

We have developed a working prototype here: http://qtrplaza.net

We originally went with a fun and young identity while we were testing, but we are shifting our focus to a more professional b2b product. Our name originally was Pals n/Perks and our designed catered more towards the end-users of our product (the people receiving the promotions) - now, we'd like to change out identity and our branding to focus more on the businesses purchasing our product. So, we've changed our name to Ripple Kindler and we are looking for a very slick and professional design to go with our new name.

We like the look of these two sites:

http://shiftlark.com
http://mailorbitly.com

To imitate the design from shiftlark.com with our software, I've created this mock-up:

http://qtrplaza.net/ripplekindler

We like these clean, professional design examples. These examples should only be used as a point of reference.

We will have approx. 8 screens in total that we will need designs for. For now, please create a web design and logo for Ripple Kindler based on these two pages:

Home Page & Promo Manager - http://qtrplaza.net/briefhub.html

Thank you!!!
Updates

Reason: we have not gotten enough designs to choose from yet to make our decision

Reason: We have not received enough unique submissions.

Thank you all for your submissions! Please recheck our brief as we have updated it.

For all the designers that have submitted designs for our project please go look at our likes and dislikes that I have uploaded. We have narrowed it down to 3 designers. Can you take our feedback into consideration and give us a more refined revision of your work and we will move forward from there. We would like to wrap this project up very soon. Thanks!                                   

Reason: We have narrowed our project submissions down to 3 designers. Please read our new posting and view our uploaded examples and what we like about each and please give us some revisions. We would like to get this project finished very soon. Thank You!

Target Market(s)

Small to Medium-Sized Business owners who are looking at marketing their business online.

Industry/Entity Type

It Company

Requirements
Must have
• Clean-professional look

Logo for Ripple Kindler

```html
<!DOCTYPE html>
<html lang="en">
<head>
<meta charset="utf-8">
<title>Ripple Kindler – Viral Marketing Software</title>
<link rel="stylesheet" href="https://fonts.googleapis.com/css2?family=Arimo:wght@400;700&family=Lato:wght@400;700&family=Open+Sans:wght@400;600&display=swap">
<style>
  :root {
    --navy: #2d2a5c;
    --orange: #f27a1f;
    --ink: #2b2b2b;
    --grey-text: #8a8a8a;
    --nav-text: #7a7a7a;
    --rule: #dcdcdc;
    --page: #f3f3f3;
    --mid-top: #f4f6f9;
    --mid-bottom: #cfd9e5;
    --tile: rgba(255,255,255,0.45);
    --footer-bg: #ececec;
    --button-grey: #6d6f73;
  }
  * { margin: 0; padding: 0; box-sizing: border-box; }
  html, body { width: 963px; height: 1200px; overflow: hidden; }
  body {
    position: relative;
    background: linear-gradient(180deg, #fafafa 0%, var(--page) 100%);
    font-family: "Open Sans", Arial, sans-serif;
    color: var(--ink);
  }
  .abs { position: absolute; }
  .top-bar { left: 0; top: 0; width: 963px; height: 5px; background: #4a4a4a; }

  /* header */
  .brand { left: 91px; top: 44px; display: flex; align-items: center; gap: 14px; }
  .brand-dot { width: 40px; height: 40px; border-radius: 50%; background: var(--orange); }
  .brand-name { font-family: "Lato", sans-serif; font-weight: 700; font-size: 40px; line-height: 1; color: var(--navy); letter-spacing: -0.5px; }

  .main-nav { left: 489px; top: 47px; width: 450px; height: 43px; border-bottom: 1px solid var(--rule); font-size: 12.5px; }
  .main-nav a { position: absolute; top: 0; text-decoration: none; color: var(--nav-text); line-height: 43px; white-space: nowrap; }
  .main-nav a.is-active { left: 0; width: 58px; text-align: center; background: var(--orange); color: #fff; box-shadow: 0 2px 0 #d5621a; }

  /* hero */
  .hero-device { left: 0; top: 138px; width: 530px; height: 282px; }
  .device-screen { left: 72px; top: 0; width: 386px; height: 260px; border-radius: 14px 14px 0 0;
    background: linear-gradient(180deg, #d9d9d9 0%, #c3c9d3 12%, #9ea6b4 55%, #b7bcc5 100%); border: 9px solid #cfcfcf; }
  .device-base { left: 0; top: 258px; width: 530px; height: 22px; border-radius: 0 0 60px 60px / 0 0 20px 20px;
    background: linear-gradient(180deg, #e6e6e6 0%, #bdbdbd 60%, #8f8f8f 100%); }
  .slider-dots { left: 239px; top: 436px; display: flex; gap: 5px; }
  .slider-dots span, .client-dots span { width: 11px; height: 11px; border-radius: 50%; background: #d3d3d3; }
  .slider-dots span.on, .client-dots span.on { background: var(--orange); }

  .hero-kicker { left: 523px; top: 150px; font-family: "Arimo", sans-serif; font-weight: 700; font-size: 26px; color: #5a5a5a; }
  .hero-title { left: 521px; top: 178px; font-family: "Arimo", sans-serif; font-weight: 700; font-size: 65px; letter-spacing: -1px; color: var(--navy); }
  .hero-copy { left: 524px; top: 262px; width: 410px; font-family: "Arimo", sans-serif; font-size: 16.5px; line-height: 22px; color: #555; }
  .hero-link { top: 351px; font-family: "Arimo", sans-serif; font-size: 19px; text-decoration: underline; text-underline-offset: 3px; }
  .hero-link.video { left: 527px; color: var(--orange); }
  .hero-link.pricing { left: 693px; color: var(--navy); }
  .learn-more { left: 791px; top: 434px; width: 138px; height: 34px; background: var(--orange); color: #fff; font-size: 12.5px; text-align: center; line-height: 34px; box-shadow: 0 2px 0 #d5621a; text-decoration: none; }
  .rule { height: 1px; background: var(--rule); left: 40px; width: 899px; }

  /* services band */
  .services-band { left: 0; top: 468px; width: 963px; height: 320px; background: linear-gradient(180deg, var(--mid-top) 0%, var(--mid-bottom) 100%); border-bottom: 1px solid #c5cfdb; }
  .intro-title { left: 38px; top: 512px; font-family: "Lato", sans-serif; font-weight: 700; font-size: 23.5px; color: var(--navy); background: #fff; padding: 0 4px 0 2px; }
  .intro-copy { left: 40px; width: 424px; font-size: 12px; line-height: 17.2px; color: var(--grey-text); }
  .more-btn { left: 40px; top: 713px; width: 57px; height: 27px; background: var(--button-grey); color: #fff; font-size: 12px; text-align: center; line-height: 27px; }
  .service-tile { width: 211px; height: 110px; background: var(--tile); display: flex; align-items: center; }
  .service-icon { width: 52px; height: 58px; margin: 0 20px 0 22px; border-radius: 5px; background: linear-gradient(180deg, #d4d6da 0%, #8d9096 60%, #5e6166 100%); }
  .service-name { font-family: "Lato", sans-serif; font-weight: 700; font-size: 14px; line-height: 16px; color: var(--ink); }

  /* bottom */
  .lower-band { left: 0; top: 789px; width: 963px; height: 411px; background: var(--footer-bg); }
  .col-title { top: 820px; font-family: "Lato", sans-serif; font-weight: 700; font-size: 16px; color: var(--ink); }
  .client-name { font-family: "Open Sans", sans-serif; font-weight: 600; color: #8e8e8e; white-space: nowrap; }
  .client-dots { left: 40px; top: 1016px; display: flex; gap: 6px; }
  .tweet { left: 346px; width: 270px; font-size: 12.5px; line-height: 17.5px; color: var(--grey-text); }
  .tweet time { display: block; font-size: 10.5px; color: var(--ink); margin-bottom: 2px; }
  .tweet a { color: #ef5a2a; text-decoration: none; }
  .testimonial-nav { left: 877px; top: 838px; }
  .quote-mark { left: 648px; top: 880px; font-family: "Arimo", sans-serif; font-weight: 700; font-size: 86px; line-height: 1; color: #9a9a9a; }
  .testimonial-text { left: 710px; top: 894px; width: 222px; font-size: 12px; line-height: 17.5px; color: #9a9a9a; }
  .testimonial-author { left: 710px; top: 996px; font-size: 10.5px; color: var(--ink); }

  .footer-social { left: 335px; top: 1133px; display: flex; align-items: center; gap: 4px; font-size: 12.5px; color: #aaa; }
  .footer-social span.icon { width: 15px; height: 15px; border-radius: 2px; background: #8a8a8a; }
  .footer-social .label { margin-right: 8px; }
  .footer-legal { left: 541px; top: 1133px; font-size: 12px; color: #555; }
  .footer-legal a { color: #777; text-decoration: none; }
</style>
</head>
<body>
  <div class="abs top-bar"></div>

  <header>
    <div class="abs brand"><span class="brand-dot"></span><span class="brand-name">Ripple Kindler</span></div>
    <nav class="abs main-nav">
      <a class="is-active" href="#">Home</a>
      <a href="#" style="left:74px">Services</a>
      <a href="#" style="left:151px">Products</a>
      <a href="#" style="left:229px">Partners</a>
      <a href="#" style="left:306px">Company</a>
      <a href="#" style="left:388px">Contacts</a>
    </nav>
  </header>

  <section class="hero">
    <div class="abs hero-device" role="img" aria-label="Laptop showing the promo manager dashboard with a share-to-get-coupon popup">
      <div class="abs device-screen"></div>
      <div class="abs device-base"></div>
    </div>
    <div class="abs slider-dots"><span></span><span class="on"></span><span></span><span></span></div>
    <div class="abs hero-kicker">Viral Marketing Software</div>
    <h1 class="abs hero-title">Reimagined.</h1>
    <p class="abs hero-copy">Ripple Kindler is a new way for businesses to handle viral marketing using the web, targeted promotions, QR codes, email and social media.</p>
    <a class="abs hero-link video" href="#">Watch the Video</a>
    <a class="abs hero-link pricing" href="#">Pricing/Packages</a>
    <a class="abs learn-more" href="#">Click to learn more</a>
    <div class="abs rule" style="top:467px"></div>
  </section>

  <section>
    <div class="abs services-band"></div>
    <h2 class="abs intro-title">GO VIRAL WITH A FEW CLICKS!</h2>
    <p class="abs intro-copy" style="top:557px">Lorem ipsum dolor sit amet, consec tetuer adipiscing elit. Praesent vestibulum molestie lacus. Aenean nonummy hendrerit mauris. Pha sellus porta. Fusce suscipit varius mi.</p>
    <p class="abs intro-copy" style="top:626px">Cum sociis natoque penatibus et magnis dis parturient montes, na scetur ridiculus mus. Nulla dui. Fusce feugiat malesuada odio. Morbi nunc odio, gravida at, cursus nec, luctus a, lorem. Maecenas tris tique orci ac sem. Duis ultricies pharetra magna.</p>
    <div class="abs more-btn">More</div>

    <div class="abs service-tile" style="left:498px;top:504px"><span class="service-icon" role="img" aria-label="Calculator icon"></span><span class="service-name">MANAGEMENT<br>CONSULTING</span></div>
    <div class="abs service-tile" style="left:727px;top:504px"><span class="service-icon" role="img" aria-label="Spiral notebook icon"></span><span class="service-name">MARKET<br>ASSESSMENT</span></div>
    <div class="abs service-tile" style="left:498px;top:628px"><span class="service-icon" role="img" aria-label="Wall clock icon"></span><span class="service-name">PROGRAM<br>MANAGEMENT</span></div>
    <div class="abs service-tile" style="left:727px;top:628px"><span class="service-icon" role="img" aria-label="Briefcase icon"></span><span class="service-name">REGULATORY<br>SUPPORT</span></div>
  </section>

  <section>
    <div class="abs lower-band"></div>

    <h3 class="abs col-title" style="left:40px">CLIENTS</h3>
    <span class="abs client-name" style="left:40px;top:893px;font-size:14px">Harborstay</span>
    <span class="abs client-name" style="left:172px;top:886px;font-size:18px">Pixelvault</span>
    <span class="abs client-name" style="left:40px;top:938px;font-size:27px">Searchly</span>
    <span class="abs client-name" style="left:168px;top:944px;font-size:18px">Medivance</span>
    <div class="abs client-dots"><span class="on"></span><span></span><span></span></div>

    <h3 class="abs col-title" style="left:346px">LATEST TWEETS</h3>
    <div class="abs tweet" style="top:895px"><time>about a day ago</time>we were checking out<br>Full Site. Quick Start Guide <a href="#">docs.sitekit-guide.com/help/full-site…</a></div>
    <div class="abs tweet" style="top:986px"><time>about 2 days ago</time>we were checking out<br>WordPress. Quick Start Guide <a href="#">docs.sitekit-guide.com/help/wordpress…</a></div>

    <h3 class="abs col-title" style="left:651px">TESTIMONIALS</h3>
    <svg class="abs testimonial-nav" width="46" height="24" viewBox="0 0 46 24" aria-label="Previous and next">
      <polyline points="16,3 6,12 16,21" fill="none" stroke="#fff" stroke-width="3"/>
      <polyline points="30,3 40,12 30,21" fill="none" stroke="#fff" stroke-width="3"/>
    </svg>
    <div class="abs quote-mark">&ldquo;</div>
    <p class="abs testimonial-text">Lorem ipsum dolor sit amet, consec tetuer adipiscing elit. Praesent ves tibulum molestie lacus. Aenean non ummy hendrerit mauris. Pha sellus porta. Fusce suscipit varius mi.</p>
    <div class="abs testimonial-author">Jamie Mallory</div>

    <div class="abs rule" style="top:1080px"></div>
  </section>

  <footer>
    <div class="abs footer-social"><span class="label">Social:</span><span class="icon"></span><span class="icon"></span><span class="icon"></span><span class="icon"></span></div>
    <div class="abs footer-legal">© 2012 <a href="#">Privacy Policy</a></div>
  </footer>
</body>
</html>
```